I need a SEO-friendly Wordpress website (making sure to style H1, H2, H3, etc correctly) for a Hawaii-based law firm called Meridale Crown Legal Group. Comparable websites include https://brvtlaw.com/ and https://www.lorvin.com/ for design reference. The current copy on the TuvellAttorney.com website can be used.

Coding

Coded - Design and coding required

```html
<!DOCTYPE html>
<html lang="en">
<head>
<meta charset="utf-8">
<title>Meridale Crown Legal Group — Kona Lawyers</title>
<link href="https://fonts.googleapis.com/css2?family=Merriweather:wght@400;700&family=Lato:wght@300;400;700&display=swap" rel="stylesheet">
<style>
:root{
  --gold:#b88a4a;
  --gold-light:#c9a063;
  --ink:#222222;
  --text:#333333;
  --muted:#8a8a8a;
  --line:#e3e3e3;
  --field:#f4f4f4;
  --footer:#2c2c2c;
  --footer-text:#8c8c8c;
  --white:#ffffff;
}
*{box-sizing:border-box;margin:0;padding:0}
html,body{width:1200px;height:3710px;overflow:hidden}
body{font-family:'Lato',sans-serif;color:var(--text);background:var(--white);position:relative}
a{text-decoration:none;color:inherit}
.serif{font-family:'Merriweather',serif}
section,header,footer{position:absolute;left:0;width:1200px}
.abs{position:absolute}

/* header */
.site-header{top:0;height:131px}
.brand{left:72px;top:30px}
.brand-name{font-family:'Merriweather',serif;font-size:29px;color:var(--ink);letter-spacing:.3px}
.brand-tag{font-size:19px;color:var(--gold);margin-top:10px;margin-left:55px}
.call{right:72px;top:25px;font-size:23px;color:var(--ink)}
.call a{color:var(--gold);text-decoration:underline}
.main-nav{right:72px;top:74px;display:flex;gap:38px;font-size:17px;color:var(--ink)}
.main-nav .active{color:var(--gold);border-bottom:2px solid var(--gold);padding-bottom:6px}
.main-nav .caret{font-size:11px}

/* hero */
.hero{top:131px;height:563px;overflow:hidden}
.hero-media{position:absolute;inset:0;background:linear-gradient(100deg,#4a3f55 0%,#5d4f66 35%,#6b5b5e 60%,#3e3440 100%)}
.hero-badge{left:86px;top:116px;background:var(--gold);color:var(--white);font-size:15px;padding:12px 21px;text-transform:uppercase}
.hero-title{left:86px;top:178px;font-family:'Merriweather',serif;font-size:34px;line-height:46px;color:var(--white);font-weight:700;width:380px}
.hero-text{left:88px;top:326px;font-size:19px;line-height:28px;color:var(--white);width:360px}
.link-more{font-size:16px;text-transform:uppercase;padding-bottom:6px;border-bottom:1px solid currentColor;display:inline-flex;gap:10px;align-items:center}
.hero .link-more{position:absolute;left:88px;top:420px;color:var(--white)}

/* practice */
.practice{top:738px;height:865px}
.practice-media{left:0;top:0;width:620px;height:865px;background:linear-gradient(90deg,#f6f6f6 0%,#e7e9ec 45%,#f5f5f5 100%)}
.practice-title{left:702px;top:70px;font-family:'Merriweather',serif;font-size:50px;color:var(--ink)}
.practice-item{left:702px;width:430px;display:flex;gap:42px}
.practice-item svg{flex:none;margin-top:2px}
.practice-item h3{font-size:23px;font-weight:400;color:var(--ink);margin-bottom:10px}
.practice-item p{font-size:15px;line-height:23px;color:var(--muted);width:310px}

/* testimonial */
.testimonial{top:1603px;height:344px;overflow:hidden}
.testimonial-media{position:absolute;inset:0;background:linear-gradient(180deg,#a7834a 0%,#b8925a 50%,#a8824c 100%)}
.quote{top:112px;left:0;width:1200px;text-align:center;color:var(--white)}
.quote p{font-size:19px;line-height:27px;width:940px;margin:0 auto}
.quote .who{font-size:18px;margin-top:25px;text-transform:uppercase}
.quote .case{font-size:15px;margin-top:10px}

/* about */
.about{top:1947px;height:666px}
.about-title{left:136px;top:80px;font-family:'Merriweather',serif;font-size:50px;line-height:60px;color:var(--ink);width:440px}
.about-sub{left:134px;top:215px;font-size:19px;font-weight:700;color:var(--gold)}
.about-copy{left:132px;top:276px;width:500px;font-size:15px;line-height:23px;color:var(--muted)}
.about-copy p+p{margin-top:15px}
.about .link-more{position:absolute;left:136px;top:560px;color:var(--gold)}
.attorney-photo{left:737px;top:73px;width:341px;height:273px;background:linear-gradient(135deg,#3a4a5a 0%,#6a6f78 45%,#2b3440 100%)}
.attorney-name{left:737px;width:341px;top:370px;text-align:center;font-size:15px;color:var(--ink);text-transform:uppercase}
.attorney-role{left:737px;width:341px;top:397px;text-align:center;font-size:15px;color:var(--muted)}

/* map */
.location{top:2613px;height:316px;overflow:hidden}
.map-media{position:absolute;inset:0;background:linear-gradient(100deg,#eceae4 0%,#dfe6ee 40%,#a9c4ea 55%,#e8e8e2 80%,#dfe8d4 100%)}
.map-pin{left:561px;top:153px;width:13px;height:13px;border-radius:50%;background:var(--gold)}
.map-address{left:593px;top:132px;width:442px;height:50px;background:var(--white);border-radius:25px;box-shadow:0 2px 10px rgba(0,0,0,.12);font-size:12px;color:var(--ink);display:flex;align-items:center;justify-content:center;text-transform:uppercase}

/* contacts */
.contacts{top:2929px;height:463px}
.contacts-title{left:137px;top:80px;font-size:32px;color:var(--ink);font-weight:400}
.contacts-intro{left:137px;top:150px;width:330px;font-size:12px;line-height:23px;color:var(--text)}
.contact-label{left:137px;font-size:8px;letter-spacing:1px;color:var(--muted);text-transform:uppercase}
.contact-value{left:137px;font-size:12px;color:var(--text)}
.field{background:var(--field);border:1px solid var(--line);font-size:12px;color:#9a9a9a;display:flex;align-items:center;gap:12px;padding:0 18px;font-family:'Lato',sans-serif}
.field-name{left:612px;top:79px;width:205px;height:39px}
.field-email{left:826px;top:79px;width:207px;height:39px}
.field-message{left:612px;top:132px;width:421px;height:157px;align-items:flex-start;padding-top:16px}
.send{left:612px;top:306px;width:140px;height:40px;border-radius:20px;background:var(--gold);color:var(--white);font-size:10px;letter-spacing:2px;font-weight:700;display:flex;align-items:center;justify-content:center}

/* footer */
.site-footer{top:3392px;height:318px;background:var(--footer)}
.footer-col{top:73px}
.footer-col h4{font-size:11px;letter-spacing:2.5px;color:var(--white);font-weight:700;text-transform:uppercase;margin-bottom:22px}
.footer-col li{list-style:none;font-size:12px;color:var(--footer-text);margin-bottom:17px}
.newsletter{left:862px;top:115px;width:208px;height:36px;border-radius:18px;background:#373737;font-size:12px;color:var(--footer-text);padding-left:22px;display:flex;align-items:center}
.newsletter-btn{position:absolute;right:0;top:1px;width:34px;height:34px;border-radius:50%;background:var(--gold);display:flex;align-items:center;justify-content:center}
.copyright{left:134px;top:273px;font-size:11px;color:var(--footer-text)}
</style>
</head>
<body>

<header class="site-header">
  <div class="abs brand">
    <div class="brand-name">Meridale Crown Legal Group</div>
    <div class="brand-tag">Divorce and Personal Injury Lawyers</div>
  </div>
  <div class="abs call">Call Today: <a href="tel:+18085550143">+1.808.555.0143</a></div>
  <nav class="abs main-nav">
    <a class="active" href="#">Home</a>
    <a href="#">Practice Areas <span class="caret">&#8964;</span></a>
    <a href="#">Attorneys</a>
    <a href="#">Blog</a>
    <a href="#">Contact Us</a>
  </nav>
</header>

<section class="hero">
  <div class="hero-media" role="img" aria-label="Bronze statue of Lady Justice holding scales in front of a shelf of law books"></div>
  <div class="abs hero-badge">Over 70 years of combined practice</div>
  <h1 class="abs hero-title">Kona Lawyers of MCLG -Legal Kōkua with Aloha</h1>
  <p class="abs hero-text">Dedicated to making sure you receive the care and attention you need.</p>
  <a class="link-more" href="#">Learn more <span>&rarr;</span></a>
</section>

<section class="practice">
  <div class="abs practice-media" role="img" aria-label="Portrait of a smiling attorney in a grey suit with arms crossed"></div>
  <h2 class="abs practice-title">Areas of Practice</h2>

  <div class="abs practice-item" style="top:193px">
    <svg width="68" height="68" viewBox="0 0 68 68" fill="none" stroke="#b88a4a" stroke-width="2.5"><rect x="8" y="10" width="30" height="14" rx="2" transform="rotate(40 23 17)"/><line x1="26" y1="26" x2="52" y2="50"/><rect x="6" y="54" width="34" height="6"/><rect x="10" y="48" width="26" height="6"/></svg>
    <div><h3>Family &amp; Divorce</h3><p>Our lawyers handle all aspects of family law on the Big Island and neighboring islands</p></div>
  </div>
  <div class="abs practice-item" style="top:351px">
    <svg width="68" height="68" viewBox="0 0 68 68" fill="none" stroke="#b88a4a" stroke-width="2.5"><rect x="8" y="10" width="30" height="14" rx="2" transform="rotate(40 23 17)"/><line x1="26" y1="26" x2="52" y2="50"/><rect x="6" y="54" width="34" height="6"/><rect x="10" y="48" width="26" height="6"/></svg>
    <div><h3>Personal Injury</h3><p>MCLG's Kona Lawyers are well-versed in torts law and have expertise in all aspects of personal injury.</p></div>
  </div>
  <div class="abs practice-item" style="top:512px">
    <svg width="68" height="68" viewBox="0 0 68 68" fill="none" stroke="#b88a4a" stroke-width="2.5"><rect x="8" y="10" width="30" height="14" rx="2" transform="rotate(40 23 17)"/><line x1="26" y1="26" x2="52" y2="50"/><rect x="6" y="54" width="34" height="6"/><rect x="10" y="48" width="26" height="6"/></svg>
    <div><h3>Corporate &amp; IP</h3><p>The attorneys at MCLG have been helping Big Island business owners with all their legal needs.</p></div>
  </div>
  <div class="abs practice-item" style="top:670px">
    <svg width="68" height="68" viewBox="0 0 68 68" fill="none" stroke="#b88a4a" stroke-width="2.5"><rect x="8" y="10" width="30" height="14" rx="2" transform="rotate(40 23 17)"/><line x1="26" y1="26" x2="52" y2="50"/><rect x="6" y="54" width="34" height="6"/><rect x="10" y="48" width="26" height="6"/></svg>
    <div><h3>Real Estate</h3><p>Our lawyers work with home owners, buyers and property developers to ensure timely handling of all legal aspects involved in real estate.</p></div>
  </div>
</section>

<section class="testimonial">
  <div class="testimonial-media" role="img" aria-label="Gavel resting in front of rows of leather-bound law books, tinted gold"></div>
  <blockquote class="abs quote">
    <p>“Lorem ipsum dolor sit amet, consectetur adipiscing elit. Nam a consectetur orci. Vivamus non metus tempus, sollicitudin odio vel, vehicula nulla. Nam ultricies sit amet nulla eu fringilla.”</p>
    <div class="who">Maren L. Okabe</div>
    <div class="case">Real Estate Case</div>
  </blockquote>
</section>

<section class="about">
  <h2 class="abs about-title">About the Kona Lawyers of MCLG</h2>
  <h3 class="abs about-sub">Lawyers Serving the Big Island and Neighboring Islands</h3>
  <div class="abs about-copy">
    <p>The experienced attorneys in the Meridale Crown Legal Group's Kailua Kona, Hawaii office provide clients with a wide range of litigation expertise, including legal claims involving divorce &amp; family, personal injury, toxic exposures, intellectual property, and real estate.</p>
    <p>Our Kona office also offers commercial and hospitality litigation expertise on behalf of a wide variety of clients, including restaurants, hotels, property owners, and many others. We never wish to see our clients go to court, though if there is no other option, you're in safe hands with our seasoned trial lawyers and the many years of courtroom experience behind them.</p>
  </div>
  <a class="link-more" href="#">Learn more <span>&rarr;</span></a>
  <div class="abs attorney-photo" role="img" aria-label="Portrait photo of the lead attorney in a dark suit and blue tie"></div>
  <div class="abs attorney-name">Daniel Ferreira, Esq</div>
  <div class="abs attorney-role">Attorney of Kona-Based MCLG</div>
</section>

<section class="location">
  <div class="map-media" role="img" aria-label="Street map of Kailua Kona showing the office location"></div>
  <div class="abs map-pin"></div>
  <div class="abs map-address">75-1820 Palani Road, Suite 210 Kailua Kona, Hawaii 96740</div>
</section>

<section class="contacts">
  <h2 class="abs contacts-title">Contacts Us</h2>
  <p class="abs contacts-intro">Lorem ipsum dolor sit amet, consectetur adipiscing elit. Fusce sapien risus, congue vitae lectus a, lacinia posuere dui. Quisque sed viverra mauris.</p>
  <div class="abs contact-label" style="top:244px">Address:</div>
  <div class="abs contact-value" style="top:264px">75-1820 Palani Road, Suite 210 Kailua Kona, Hawaii 96740.</div>
  <div class="abs contact-label" style="top:305px">Phone:</div>
  <div class="abs contact-value" style="top:324px">+1.808.555.0143</div>
  <div class="abs contact-label" style="top:367px">Email:</div>
  <div class="abs contact-value" style="top:386px">clients@tuvellattorney.com</div>

  <div class="abs field field-name">
    <svg width="12" height="12" viewBox="0 0 12 12" fill="#b5b5b5"><circle cx="6" cy="3.5" r="3"/><path d="M0 12c0-4 3-5.5 6-5.5S12 8 12 12z"/></svg>Name
  </div>
  <div class="abs field field-email">
    <svg width="14" height="10" viewBox="0 0 14 10" fill="#b5b5b5"><rect width="14" height="10" rx="1"/><path d="M1 1l6 5 6-5" stroke="#f4f4f4" stroke-width="1.3" fill="none"/></svg>E-mail
  </div>
  <div class="abs field field-message">Your Message</div>
  <a class="abs send" href="#">SEND</a>
</section>

<footer class="site-footer">
  <div class="abs footer-col" style="left:134px">
    <h4>Learn more</h4>
    <ul><li>Home</li><li>Practices Areas</li><li>Attorneys</li><li>Blog</li></ul>
  </div>
  <div class="abs footer-col" style="left:346px">
    <h4>Information</h4>
    <ul><li>About Us</li><li>FAQs</li><li>Privacy Policy</li><li>Terms &amp; Conditions</li></ul>
  </div>
  <div class="abs footer-col" style="left:557px">
    <h4>Get in touch</h4>
    <ul><li>Contact Us</li><li>Customer Service</li></ul>
  </div>
  <div class="abs footer-col" style="left:862px">
    <h4>Subscribe to newsletter</h4>
  </div>
  <div class="abs newsletter">E-mail
    <span class="newsletter-btn"><svg width="14" height="10" viewBox="0 0 14 10" fill="none" stroke="#fff" stroke-width="1.4"><rect x=".7" y=".7" width="12.6" height="8.6" rx="1"/><path d="M1 1.5l6 4.5 6-4.5"/></svg></span>
  </div>
  <div class="abs copyright">© 2019 Meridale Crown Legal Group. All rights reserved.</div>
</footer>

</body>
</html>
```